依頼詳細
上品なイメージで、男女共に使えるようにお願いします。
ハガキ中のどこかに、新居のパースを入れられるように場所を確保して下さい。(吹き出しや枠組みなどでサンプルを入れておいて頂ければお客様毎にこちらで差替を致します)
下の文面に加え、住所・氏名を入れる欄を作成下さい。
記載項目
転居のおしらせ

念願叶って、新築住宅が完成し転居致しました。
取り急ぎお知らせ致します。
今後とも変わらぬおつきあいを頂けますよう
よろしくお願い致します。
お近くにお越しの際にはお気軽にお立ち寄り下さい。
希望イメージ
• +5 0 +5
• シンプル
複雑
• 単色
カラフル
• 暗い
明るい
• 日常
高級
• 遊び心
厳粛
• 未来的
伝統的
• 女性的
男性的
希望する色
赤系、緑系
納品ファイル
• イラストレーター形式 (.ai)
補足説明
依頼公開後の追記内容
■ 選んだ理由

明るく、万人受けする雰囲気で、カジュアルすぎず、我が社のイメージと合っていた。
また、パースの入替もしやすかった。

■ 提案者全員のお礼・コメント

ご提案ありがとうございます。
また、今後とも様々な依頼を行っていきたいと思いますのでよろしくお願い致します。

```html
<!DOCTYPE html>
<html lang="ja">
<head>
<meta charset="UTF-8">
<title>転居のおしらせ</title>
<link href="https://fonts.googleapis.com/css2?family=M+PLUS+Rounded+1c:wght@500;800&family=Montserrat:wght@800&display=swap" rel="stylesheet">
<style>
  :root{
    --page:#b3b3b3;
    --card:#ffffff;
    --beige:#f3ead6;
    --pink:#f6e1dc;
    --title:#6b4a2b;
    --text:#4a3b2e;
    --ghost:#e4d7bb;
    --ghost-pink:#ecd0c8;
    --sky:#a9c9e6;
    --house:#ebe9e4;
    --green:#8fb478;
    --town:#c3cfd9;
    --town-low:#b2c2cf;
    --rule:#cfcfcf;
  }
  *{margin:0;padding:0;box-sizing:border-box}
  html,body{width:857px;height:1200px;overflow:hidden;background:var(--page)}
  body{position:relative;font-family:"M PLUS Rounded 1c",sans-serif}
  .postcard{position:absolute;left:149px;width:580px;height:394px;background:var(--card);box-shadow:0 2px 6px rgba(0,0,0,.25)}
  .postcard--beige{top:143px}
  .postcard--pink{top:643px}
  .panel{position:absolute;left:18px;top:18px;width:544px;height:320px;border-radius:14px;background:var(--tone)}
  .postcard--beige .panel{--tone:var(--beige)}
  .postcard--pink .panel{--tone:var(--pink)}
  .ghost-heading{position:absolute;left:30px;top:22px;font-family:"Montserrat",sans-serif;font-weight:800;font-size:40px;letter-spacing:2px;line-height:1;color:var(--ghost)}
  .postcard--pink .ghost-heading{color:var(--ghost-pink)}
  .title{position:absolute;left:54px;top:48px;font-weight:800;font-size:24px;line-height:1.2;color:var(--title);letter-spacing:2px}
  .message{position:absolute;left:30px;top:92px;width:270px;text-align:center;font-weight:500;font-size:13.5px;line-height:23px;color:var(--text)}
  .house-photo{position:absolute;left:318px;top:28px;width:236px;height:222px;border-radius:14px;
    background:linear-gradient(180deg,var(--sky) 0%,#d6e4f0 45%,var(--house) 62%,var(--green) 100%)}
  .family-photo{position:absolute;left:456px;top:250px;width:98px;height:98px;border-radius:50%;border:4px solid #fff;
    background:radial-gradient(circle at 50% 40%,#f0e3d6,#c2cfae)}
  .townscape{position:absolute;left:26px;top:272px;width:380px;height:46px;border-radius:4px;
    background:linear-gradient(180deg,var(--town) 0%,var(--town-low) 100%)}
  .divider{position:absolute;left:330px;top:346px;width:1px;height:34px;background:var(--rule)}
  .postal{position:absolute;left:30px;top:364px;font-size:10px;color:var(--text)}
  .family-name{position:absolute;right:26px;top:362px;font-size:11px;color:var(--text)}
</style>
</head>
<body>
  <section class="postcard postcard--beige">
    <div class="panel"></div>
    <div class="ghost-heading">WE MOVED</div>
    <h1 class="title">転居のおしらせ</h1>
    <p class="message">念願叶って、新築住宅が完成し<br>転居致しました。<br>取り急ぎお知らせ致します。<br>今後とも変わらぬおつきあいを<br>頂けますようよろしくお願い致します。<br>お近くにお越しの際には<br>お気軽にお立ち寄り下さい。</p>
    <div class="house-photo" role="img" aria-label="新居のパース（白い外壁の二階建て住宅と青空）"></div>
    <div class="townscape" role="img" aria-label="色とりどりの家が並ぶ街並みのイラスト"></div>
    <div class="family-photo" role="img" aria-label="家族の写真"></div>
    <div class="divider"></div>
    <p class="postal">〒000-0000</p>
    <p class="family-name">山本 家</p>
  </section>

  <section class="postcard postcard--pink">
    <div class="panel"></div>
    <div class="ghost-heading">WE MOVED</div>
    <h1 class="title">転居のおしらせ</h1>
    <p class="message">念願叶って、新築住宅が完成し<br>転居致しました。<br>取り急ぎお知らせ致します。<br>今後とも変わらぬおつきあいを<br>頂けますようよろしくお願い致します。<br>お近くにお越しの際には<br>お気軽にお立ち寄り下さい。</p>
    <div class="house-photo" role="img" aria-label="新居のパース（白い外壁の二階建て住宅と青空）"></div>
    <div class="townscape" role="img" aria-label="色とりどりの家が並ぶ街並みのイラスト"></div>
    <div class="family-photo" role="img" aria-label="家族の写真"></div>
    <div class="divider"></div>
    <p class="postal">〒000-0000</p>
    <p class="family-name">山本 家</p>
  </section>
</body>
</html>
```